VORLEK TPMS
Website design
VORLEK TPMS - Automotive
Creative Brief
Automotive
www.VORLEKTPMS.example
TPMS is Tire Pressure Monitor Sensor. The go inside your vehicles tires and transmit information to your dashboard indicating what your tire's air pressure is. Vorlek TPMS designs, engineers and manufactures TPMS.
LIKES: Left hand navigation by vehicle (TPMS for Brisca, TPMS for QDN, TPMS for Palverine" etc etc), Year Make Model search box in content area", Modern colors, easy to navigate, professional design. DISLIKES: Busy page, hard to navigate, cluttered look.
Elegant
Modern, new colors
left side
IMPORTANT:Please see attachment for logos and layout template.

```html
<!DOCTYPE html>
<html lang="en">
<head>
<meta charset="utf-8">
<title>Vorlek TPMS</title>
<link href="https://fonts.googleapis.com/css2?family=Arimo:wght@400;700&display=swap" rel="stylesheet">
<style>
:root{
  --red:#b3121b;
  --red-dark:#6d0a0f;
  --orange:#e38a10;
  --orange-light:#f5b640;
  --grey-text:#555;
  --grey-line:#d6d6d6;
  --footer:#3c3c3c;
}
*{box-sizing:border-box;margin:0;padding:0}
html,body{width:1200px;height:957px;overflow:hidden}
body{font-family:"Arimo",Arial,sans-serif;background:linear-gradient(#f3f3f3,#d8d8d8);position:relative;color:var(--grey-text)}
.page{position:absolute;left:176px;top:0;width:851px;height:893px;background:#fff;box-shadow:0 0 10px rgba(0,0,0,.15)}
.abs{position:absolute}
.logo{left:186px;top:18px;font-size:42px;font-weight:700;color:var(--red);letter-spacing:1px;line-height:1}
.logo small{display:block;font-size:15px;letter-spacing:13px;margin-top:4px;padding-left:12px}
.search{left:835px;top:9px;width:182px;height:20px;border:1px solid #ccc;background:#fafafa;font-size:11px;color:#aaa;padding:3px 6px}
.search svg{position:absolute;right:4px;top:3px}
.ship{left:517px;top:33px;width:503px;height:24px;background:linear-gradient(#f4f4f4,#dcdcdc);font-size:12px;color:#333;padding:0 4px 0 10px;text-align:right;white-space:nowrap;line-height:24px}
.ship b{color:var(--red);font-style:italic}
.ship .btn{display:inline-block;background:var(--red-dark);color:#fff;font-size:11px;font-weight:700;padding:0 7px;line-height:18px;margin-left:6px;font-style:normal}
.talk{left:495px;top:70px;font-size:12px;color:#333}
.talk b{color:var(--red);margin:0 6px 0 4px}
.acct{top:68px;height:22px;background:linear-gradient(var(--red),var(--red-dark));color:#fff;font-size:12px;padding:4px 10px}
.nav{left:181px;top:96px;width:173px;height:253px;background:linear-gradient(90deg,#c96e06,var(--orange));list-style:none;padding-top:4px}
.nav li{height:29px;margin:0 14px 2px;border-bottom:1px solid rgba(255,255,255,.35);color:#fff;font-size:14px;text-align:center;line-height:29px;text-transform:uppercase}
.nav li.active{background:var(--orange-light);color:#5a2a00;font-weight:700}
.banner{left:354px;top:96px;width:673px;height:253px;background:linear-gradient(90deg,#4a0508,#a8141c 45%,#7a0c12)}
.banner-photo{left:620px;top:96px;width:407px;height:253px;background:linear-gradient(120deg,#8a1218,#4a3b3c 55%,#2c2c30)}
.hero-band{left:354px;top:158px;width:380px;height:56px;background:linear-gradient(90deg,rgba(40,0,3,.55),rgba(40,0,3,0))}
.hero-title{left:378px;top:166px;color:#fff;font-size:44px;font-weight:700;letter-spacing:1px;line-height:1}
.hero-sub{left:510px;top:226px;color:#fff;font-size:48px;font-weight:400;line-height:1}
.cats{left:181px;top:356px;width:173px;height:537px;background:#f0f0f0}
.cats h3{background:linear-gradient(var(--red),var(--red-dark));color:#fff;font-size:16px;padding:7px 10px}
.cats ul{list-style:none;padding:6px 8px}
.cats li{font-size:10.5px;height:26px;line-height:26px;border-bottom:1px solid #ddd;padding-left:12px;position:relative;text-transform:uppercase;color:#444}
.cats li:before{content:"";position:absolute;left:2px;top:11px;width:4px;height:4px;background:var(--red)}
.welcome{left:375px;top:360px;width:645px}
.welcome h1{font-size:20px;color:#222;font-weight:700;border-bottom:1px solid var(--grey-line);padding-bottom:6px}
.welcome h1 span{color:var(--red)}
.welcome p{font-size:12px;line-height:15px;margin-top:8px;color:#444}
.col{top:556px;width:195px}
.col h4{font-size:19px;font-weight:700;color:#222;border-bottom:1px solid var(--grey-line);padding-bottom:4px}
.col h4 span{color:var(--red)}
.col .photo{height:82px;margin-top:10px;background:linear-gradient(135deg,#2a2a2e,#6a6e75 50%,#1f1f22)}
.col p{font-size:12px;line-height:14px;margin-top:12px;color:#444}
.col p b{color:var(--red);font-size:10px}
.tpbar{left:375px;top:768px;width:645px;height:34px;background:linear-gradient(#eee,#cfcfcf);font-size:16px;font-weight:700;color:#333;padding:8px 0 0 40px}
.tpbar span{color:var(--red);font-weight:400}
.brands{left:205px;top:808px;width:790px;height:64px;background:linear-gradient(#f4f4f4,#d9d9d9);display:flex;justify-content:space-around;align-items:center}
.brand{text-align:center;font-size:10px;color:#555}
.brand i{display:block;width:32px;height:32px;border-radius:50%;background:#8d8d8d;margin:0 auto 3px}
.footer{left:0;top:893px;width:1200px;height:64px;background:var(--footer)}
.footer-links{left:190px;top:903px;font-size:11px;color:#ddd}
.footer-copy{left:190px;top:925px;font-size:9px;color:#999}
.footer-logo{left:870px;top:905px;font-size:30px;font-weight:700;color:#bdbdbd;letter-spacing:1px}
</style>
</head>
<body>
<div class="page"></div>

<div class="abs logo">VORLEK<small>TPMS</small></div>
<div class="abs search">search...
  <svg width="12" height="12" viewBox="0 0 12 12"><circle cx="5" cy="5" r="3.5" fill="none" stroke="#b3121b" stroke-width="1.6"/><line x1="7.6" y1="7.6" x2="11" y2="11" stroke="#b3121b" stroke-width="1.8"/></svg>
</div>
<div class="abs ship">Shopping outside the US? <b>INTERNATIONAL SHIPPING</b> is now available! <span class="btn">Learn More</span></div>
<div class="abs talk">Lets talk! 24/7 Service at
  <svg width="12" height="12" viewBox="0 0 12 12"><path d="M1 3c0-1 1-2 2-2h6c1 0 2 1 2 2v1H8V3H4v1H1z M2 5h8l1 6H1z" fill="#333"/></svg><b>1.234.567.8910</b>
  <svg width="12" height="12" viewBox="0 0 12 12"><path d="M1 3c0-1 1-2 2-2h6c1 0 2 1 2 2v1H8V3H4v1H1z M2 5h8l1 6H1z" fill="#333"/></svg><b>1.234.567.8910</b>
</div>
<div class="abs acct" style="left:890px">Login</div>
<div class="abs acct" style="left:948px">Register</div>

<ul class="abs nav">
  <li class="active">Home</li><li>About us</li><li>Our services</li><li>Our products</li>
  <li>Testimonials</li><li>Partners</li><li>FAQs</li><li>Contact us</li>
</ul>

<div class="abs banner"></div>
<div class="abs banner-photo" role="img" aria-label="Mechanic servicing a red car wheel"></div>
<div class="abs hero-band"></div>
<h2 class="abs hero-title">COMPRESSED</h2>
<div class="abs hero-sub">AIR CAR</div>

<div class="abs cats">
  <h3>CATEGORIES</h3>
  <ul>
    <li>Lorem ipsum dolor sit</li><li>Amet, consectetur</li><li>Adipiscing elit. Aenean</li>
    <li>Scelerisque purus a</li><li>Magna molestie</li><li>Bibendum. In hac</li>
    <li>Habitasse platea</li><li>Dictumst. Quisque vel</li><li>Nulla at nunc mollis</li>
    <li>Varius. Curabitur</li><li>Dapibus eleifend porta.</li><li>Donec turpis sapien,</li>
    <li>Pharetra molestie</li><li>Consectetur et,</li><li>Dignissim, risus in</li>
  </ul>
</div>

<div class="abs welcome">
  <h1>WELCOME TO <span>VORLEK</span></h1>
  <p>Lorem ipsum dolor sit amet, consectetur adipisicing elit, sed do eiusmod tempor incididunt ut labore et dolore magna aliqua. Duis aute irure dolor in reprehenderit in voluptate velit esse cillum dolore eu fugiat nulla pariatur. Excepteur sint occaecat cupidatat non proident, sunt in culpa qui officia deserunt mollit anim id est laborum.</p>
  <p>Duis aute irure dolor in reprehenderit in voluptate velit esse cillum dolore eu fugiat nulla pariatur. Excepteur sint occaecat cupidatat non proident, sunt in culpa qui officia deserunt mollit anim id est laborum.</p>
</div>

<div class="abs col" style="left:375px">
  <h4>OUR <span>SERVICES</span></h4>
  <div class="photo" role="img" aria-label="Close-up of a car wheel and tire"></div>
  <p>Lorem ipsum dolor sit amet, consectetur adipisicing elit, sed do eiusmod <b>READ MORE...</b></p>
</div>
<div class="abs col" style="left:593px">
  <h4>OUR <span>PRODUCTS</span></h4>
  <div class="photo" role="img" aria-label="Close-up of a car wheel and tire"></div>
  <p>Lorem ipsum dolor sit amet, consectetur adipisicing elit, sed do eiusmod <b>READ MORE...</b></p>
</div>
<div class="abs col" style="left:812px">
  <h4>OUR <span>ACCESSORIES</span></h4>
  <div class="photo" role="img" aria-label="Close-up of a car wheel and tire"></div>
  <p>Lorem ipsum dolor sit amet, consectetur adipisicing elit, sed do eiusmod <b>READ MORE...</b></p>
</div>

<div class="abs tpbar">
  <svg class="abs" style="left:10px;top:10px" width="14" height="14" viewBox="0 0 14 14"><path d="M10 1L3 7l7 6z" fill="#666"/></svg>
  TIRE PRESSURE MONITER SENSOR <span>for loremipsum</span>
  <svg class="abs" style="right:10px;top:10px" width="14" height="14" viewBox="0 0 14 14"><path d="M4 1l7 6-7 6z" fill="#666"/></svg>
</div>

<div class="abs brands">
  <div class="brand"><i></i>Brisca</div><div class="brand"><i></i>Lumeran</div>
  <div class="brand"><i></i>Valdkraft</div><div class="brand"><i></i>Tomora</div>
  <div class="brand"><i></i>QDN</div><div class="brand"><i></i>Brisca</div>
  <div class="brand"><i></i>Lumeran</div><div class="brand"><i></i>Valdkraft</div>
  <div class="brand"><i></i>Tomora</div><div class="brand"><i></i>QDN</div>
</div>

<div class="abs footer"></div>
<div class="abs footer-links">HOME | ABOUT US | OUR SERVICES | OUR PRODUCTS | TESTIMONIALS | PARTNERS | FAQS | CONTACT US</div>
<div class="abs footer-copy">© 2011 www.VORLEKTPMS.example ALL RIGHTS RESERVED</div>
<div class="abs footer-logo">VORLEK TPMS</div>
</body>
</html>
```